Merry Fern Lumo alcohol cooler

I need a design using my Merry Fern Beverage Logo for 4 different styles of Malt Beverage. The cocktails are easy drinking tropical feel. We will be using the best ingredients and try to be all natural and organic.
Zaller Lime
Zaller Orange
Zaller Grapefruit
Zaller Strawberry
We would like as few colors as possible in the design.

Target Market(s)

21 - 50
Women

Requirements
Must have
• the 4 styles
• my LOGO
• label dimension inside 3"wide x 4"high maximum
• 4 pack design
• label must have 12 FL OZ
• label must have 5% ALC/VOL
Nice to have
• Clean crisp feel
Should not have
• please keep design to 3 colors or less

```html
<!DOCTYPE html>
<html lang="en">
<head>
<meta charset="utf-8">
<title>Zaller Malt Beverage Labels</title>
<link rel="stylesheet" href="https://fonts.googleapis.com/css2?family=Bree+Serif&family=Montserrat:wght@400;600&display=swap">
<style>
  :root {
    --bg-light: #d9dadb;
    --bg-dark: #b1b2b4;
    --label-dark: #2d2b2c;
    --brand-green: #2f5e45;
    --paper: #ffffff;
    --ink: #3a3a3a;
  }
  html, body {
    margin: 0;
    padding: 0;
    width: 1200px;
    height: 1200px;
    overflow: hidden;
  }
  body {
    background: radial-gradient(circle at 50% 50%, var(--bg-light) 0%, var(--bg-dark) 75%);
  }
  .label-sheet {
    position: absolute;
    left: 289px;
    top: 187px;
    display: grid;
    grid-template-columns: 305px 305px;
    grid-template-rows: 406px 406px;
    gap: 13px;
  }
  .label { display: block; width: 305px; height: 406px; }
  .brand-name {
    font-family: "Montserrat", sans-serif;
    font-weight: 600;
    fill: var(--brand-green);
    letter-spacing: 2px;
  }
  .flavor-name {
    font-family: "Bree Serif", serif;
    fill: var(--paper);
    stroke: var(--brand-green);
    stroke-width: 3px;
    paint-order: stroke;
  }
  .spec {
    font-family: "Montserrat", sans-serif;
    font-weight: 400;
    font-size: 13px;
    fill: var(--ink);
  }
</style>
</head>
<body>
<main class="label-sheet">

  <!-- Lime -->
  <svg class="label" viewBox="0 0 381 508" aria-label="Zaller Lime label">
    <defs>
      <linearGradient id="lime-band" x1="0" x2="1">
        <stop offset="0" stop-color="#0fbd3a"/><stop offset="0.45" stop-color="#8fdc3b"/><stop offset="1" stop-color="#10bd3a"/>
      </linearGradient>
    </defs>
    <rect width="381" height="508" fill="var(--paper)"/>
    <polygon points="0,0 381,0 381,282 190,300 0,282" fill="var(--label-dark)"/>
    <polygon points="0,290 150,306 0,318" fill="#17a84a"/>
    <polygon points="0,318 381,290 381,420 0,458" fill="url(#lime-band)"/>
    <polygon points="230,444 381,428 381,458" fill="#d3e03a"/>
    <circle cx="190" cy="138" r="106" fill="var(--paper)"/>
    <circle cx="190" cy="138" r="97" fill="none" stroke="var(--brand-green)" stroke-width="3"/>
    <text class="brand-name" x="190" y="132" font-size="19" text-anchor="middle">MERRY FERN</text>
    <text class="brand-name" x="190" y="158" font-size="19" text-anchor="middle">BEVERAGE</text>
    <g transform="rotate(-4 190 370)">
      <text class="flavor-name" x="190" y="367" font-size="54" text-anchor="middle">Zaller</text>
      <text class="flavor-name" x="190" y="422" font-size="54" text-anchor="middle">Lime</text>
    </g>
    <text class="spec" x="30" y="480">5% ALC/VOL</text>
    <text class="spec" x="344" y="480" text-anchor="end">12 FL OZ.</text>
  </svg>

  <!-- Orange -->
  <svg class="label" viewBox="0 0 381 508" aria-label="Zaller Orange label">
    <defs>
      <linearGradient id="orange-band" x1="0" x2="1">
        <stop offset="0" stop-color="#f7911d"/><stop offset="0.5" stop-color="#ffe014"/><stop offset="1" stop-color="#f7941d"/>
      </linearGradient>
    </defs>
    <rect width="381" height="508" fill="var(--paper)"/>
    <polygon points="0,0 381,0 381,282 190,300 0,282" fill="var(--label-dark)"/>
    <polygon points="0,290 150,306 0,318" fill="#f07b32"/>
    <polygon points="0,318 381,290 381,420 0,458" fill="url(#orange-band)"/>
    <polygon points="230,444 381,428 381,458" fill="#ffd22c"/>
    <circle cx="190" cy="138" r="106" fill="var(--paper)"/>
    <circle cx="190" cy="138" r="97" fill="none" stroke="var(--brand-green)" stroke-width="3"/>
    <text class="brand-name" x="190" y="132" font-size="19" text-anchor="middle">MERRY FERN</text>
    <text class="brand-name" x="190" y="158" font-size="19" text-anchor="middle">BEVERAGE</text>
    <g transform="rotate(-4 190 370)">
      <text class="flavor-name" x="190" y="367" font-size="54" text-anchor="middle">Zaller</text>
      <text class="flavor-name" x="190" y="422" font-size="54" text-anchor="middle">Orange</text>
    </g>
    <text class="spec" x="30" y="480">5% ALC/VOL</text>
    <text class="spec" x="344" y="480" text-anchor="end">12 FL OZ.</text>
  </svg>

  <!-- Grapefruit -->
  <svg class="label" viewBox="0 0 381 508" aria-label="Zaller Grapefruit label">
    <defs>
      <linearGradient id="grapefruit-band" x1="0" x2="1">
        <stop offset="0" stop-color="#f0261c"/><stop offset="0.55" stop-color="#f7941d"/><stop offset="1" stop-color="#f03a1e"/>
      </linearGradient>
    </defs>
    <rect width="381" height="508" fill="var(--paper)"/>
    <polygon points="0,0 381,0 381,282 190,300 0,282" fill="var(--label-dark)"/>
    <polygon points="0,290 150,306 0,318" fill="#ee5a3c"/>
    <polygon points="0,318 381,290 381,420 0,458" fill="url(#grapefruit-band)"/>
    <polygon points="230,444 381,428 381,458" fill="#ffcc2a"/>
    <circle cx="190" cy="138" r="106" fill="var(--paper)"/>
    <circle cx="190" cy="138" r="97" fill="none" stroke="var(--brand-green)" stroke-width="3"/>
    <text class="brand-name" x="190" y="132" font-size="19" text-anchor="middle">MERRY FERN</text>
    <text class="brand-name" x="190" y="158" font-size="19" text-anchor="middle">BEVERAGE</text>
    <g transform="rotate(-4 190 370)">
      <text class="flavor-name" x="190" y="367" font-size="54" text-anchor="middle">Zaller</text>
      <text class="flavor-name" x="190" y="422" font-size="54" text-anchor="middle">Grapefruit</text>
    </g>
    <text class="spec" x="30" y="480">5% ALC/VOL</text>
    <text class="spec" x="344" y="480" text-anchor="end">12 FL OZ.</text>
  </svg>

  <!-- Strawberry -->
  <svg class="label" viewBox="0 0 381 508" aria-label="Zaller Strawberry label">
    <defs>
      <linearGradient id="strawberry-band" x1="0" x2="1">
        <stop offset="0" stop-color="#ee1c9a"/><stop offset="0.5" stop-color="#f45fb5"/><stop offset="1" stop-color="#ee1c95"/>
      </linearGradient>
    </defs>
    <rect width="381" height="508" fill="var(--paper)"/>
    <polygon points="0,0 381,0 381,282 190,300 0,282" fill="var(--label-dark)"/>
    <polygon points="0,290 150,306 0,318" fill="#e3298f"/>
    <polygon points="0,318 381,290 381,420 0,458" fill="url(#strawberry-band)"/>
    <polygon points="230,444 381,428 381,458" fill="#ee4f9d"/>
    <circle cx="190" cy="138" r="106" fill="var(--paper)"/>
    <circle cx="190" cy="138" r="97" fill="none" stroke="var(--brand-green)" stroke-width="3"/>
    <text class="brand-name" x="190" y="132" font-size="19" text-anchor="middle">MERRY FERN</text>
    <text class="brand-name" x="190" y="158" font-size="19" text-anchor="middle">BEVERAGE</text>
    <g transform="rotate(-4 190 370)">
      <text class="flavor-name" x="190" y="367" font-size="54" text-anchor="middle">Zaller</text>
      <text class="flavor-name" x="190" y="422" font-size="54" text-anchor="middle" textLength="320" lengthAdjust="spacingAndGlyphs">Strawberry</text>
    </g>
    <text class="spec" x="30" y="480">5% ALC/VOL</text>
    <text class="spec" x="344" y="480" text-anchor="end">12 FL OZ.</text>
  </svg>

</main>
</body>
</html>
```